Snack package design "Lantern Curl Bites"

Looking to create a fun package design of snack. Snack is sweet and crunchy; great for people that wants to munch on stuff. Name of the Snack is "Lantern Curl Bites". The net weight should be 16oz (453 grams). I added brand "TWbR" Tiny Wonders bring Rain on the file. I also added picture of the snack. Package will be a pouch type.

Target Market(s)

People that like sweet snacks

Industry/Entity Type

Food snacks

Requirements
Must have
• Name of Snack "Lantern Curl Bites" and logo of company on top left.
Nice to have
• something that's simple and clean design

```html
<!DOCTYPE html>
<html lang="en">
<head>
<meta charset="UTF-8">
<title>Lantern Curl Bites – Pouch Front</title>
<link rel="stylesheet" href="https://fonts.googleapis.com/css2?family=Open+Sans:wght@600&family=Lobster&family=Oswald:wght@500&family=Roboto:wght@400&display=swap">
<style>
  :root {
    --backdrop: #dfe5e8;
    --pouch-yellow: #f7e431;
    --pouch-yellow-deep: #f2d92a;
    --band-green: #6d9a34;
    --tag-green: #4f8a2b;
    --tag-brown: #b7761f;
    --tag-red: #9e2230;
    --title-blue: #2f6fb0;
    --ink: #1d1d1d;
    --snack-light: #e99a55;
    --snack-mid: #d6733a;
    --snack-dark: #a8502a;
    --white: #ffffff;
  }
  * { margin: 0; padding: 0; box-sizing: border-box; }
  html, body {
    width: 1200px; height: 835px; overflow: hidden;
    background: var(--backdrop);
  }
  .canvas {
    position: relative; width: 1200px; height: 835px;
    display: flex; justify-content: center; align-items: center;
  }
  .pouch {
    position: relative; width: 470px; height: 810px;
    background: linear-gradient(180deg, var(--pouch-yellow) 0%, var(--pouch-yellow-deep) 100%);
    border-radius: 14px 14px 4px 4px;
    overflow: hidden;
  }
  .pouch-seal {
    position: absolute; left: 0; right: 0; top: 14px; height: 2px;
    background: rgba(0,0,0,0.06);
  }
  .pouch-zip {
    position: absolute; left: 0; right: 0; top: 66px; height: 3px;
    background: rgba(0,0,0,0.05);
  }
  .tagline {
    position: absolute; top: 96px; left: 0; right: 0;
    text-align: center;
    font-family: "Open Sans", sans-serif; font-weight: 600;
    font-size: 32px; line-height: 40px; letter-spacing: -0.3px;
  }
  .tagline .w1 { color: var(--tag-green); }
  .tagline .w2 { color: var(--tag-brown); }
  .tagline .w3 { color: var(--tag-red); }
  .brand-name {
    position: absolute; top: 150px; left: 0; right: 0;
    text-align: center;
    font-family: "Open Sans", sans-serif; font-weight: 600;
    font-size: 78px; line-height: 88px; color: var(--tag-green);
    letter-spacing: 6px;
  }
  .product-name {
    position: absolute; top: 262px; left: 0; right: 0;
    text-align: center;
    font-family: "Lobster", cursive; font-weight: 400;
    font-size: 48px; line-height: 52px; color: var(--white);
    text-shadow: 2px 2px 0 var(--tag-red), -1px 1px 0 var(--title-blue);
  }
  .net-weight {
    position: absolute; top: 394px; left: 0; right: 0;
    text-align: center;
    font-family: "Roboto", sans-serif; font-size: 16px; line-height: 20px; color: var(--ink);
  }
  .snack-window {
    position: absolute; left: 0; right: 0; top: 430px; bottom: 0;
  }
  .snack-window svg { display: block; width: 100%; height: 100%; }
  .claim {
    position: absolute; top: 632px; left: 0; right: 0;
    text-align: center;
    font-family: "Oswald", sans-serif; font-weight: 500;
    font-size: 34px; line-height: 44px; color: var(--white);
    text-shadow: 1px 1px 0 var(--ink), -1px -1px 0 var(--ink), 1px -1px 0 var(--ink), -1px 1px 0 var(--ink);
  }
</style>
</head>
<body>
<main class="canvas">
  <section class="pouch">
    <div class="pouch-seal"></div>
    <div class="pouch-zip"></div>

    <p class="tagline"><span class="w1">Tiny</span> <span class="w2">Wonders</span> <span class="w3">bring Rain</span></p>

    <p class="brand-name">TWbR</p>

    <h1 class="product-name">Lantern<br>Curl Bites</h1>

    <p class="net-weight">Net Weight:16oz (453 grams)</p>

    <div class="snack-window">
      <svg viewBox="0 0 470 380" preserveAspectRatio="none">
        <defs>
          <linearGradient id="snackFill" x1="0" y1="0" x2="1" y2="1">
            <stop offset="0" stop-color="var(--snack-mid)"/>
            <stop offset="0.5" stop-color="var(--snack-light)"/>
            <stop offset="1" stop-color="var(--snack-dark)"/>
          </linearGradient>
        </defs>
        <path d="M0 30 C50 10 100 2 170 8 C280 18 380 50 470 52 L470 380 L0 380 Z" fill="var(--band-green)"/>
        <path d="M0 40 C50 20 100 12 170 18 C280 28 380 60 470 62 L470 380 L0 380 Z"
              fill="url(#snackFill)" role="img" aria-label="Photo of golden sweet crunchy curl-shaped snack pieces"/>
      </svg>
    </div>

    <p class="claim">Sweet And Crunchy</p>
  </section>
</main>
</body>
</html>
```